New Software Development Firm Needs Business Cards!

We just completed a successful logo design project on MockupHive and need to develop a business card design using that shiny new logo. We want a clean, modern design that communicates professionalism and tech savvy without being cliche'.

The company is "Tersyn Works, LLC", but our dba is "Tersyn" The business card address should reflect the full company name in the address. The logo just uses "Tersyn".

Photoshop or Illustrator source files will be required, along with exact font name(s) and source(s) used.

The design will need to work well with our letterhead as well. I'm also launching a project right now for letterhead and envelopes as well. Please submit to both projects! We're excited to see the designs. Thanks...

Target Market(s)

Small to medium business professionals

Industry/Entity Type

Business

Requirements
Must have
• Need place for:
- Company name and address (5 lines)
- Phone: (1 number)
- Fax: (1 number)
- Employee's name
- Employee's position
- Employee's email address
- Company web site URL
Nice to have
• Probably want a white card, but we're open to options.

```html
<!DOCTYPE html>
<html lang="en">
<head>
<meta charset="utf-8">
<title>Tersyn Business Card</title>
<link rel="stylesheet" href="https://fonts.googleapis.com/css2?family=PT+Sans:wght@400;700&display=swap">
<style>
  :root {
    --ink: #050505;
    --paper: #ffffff;
    --accent: #ec1c24;
    --band: #58585a;
    --stage: #ffffff;
  }
  * { margin: 0; padding: 0; box-sizing: border-box; }
  html, body {
    width: 1200px; height: 1000px; overflow: hidden;
    background: var(--stage);
    font-family: "PT Sans", sans-serif;
  }
  .canvas { position: relative; width: 1200px; height: 1000px; }
  .card {
    position: absolute; left: 233px; width: 735px; height: 421px;
    overflow: hidden;
    box-shadow: 4px 6px 8px rgba(0,0,0,0.35);
  }
  .card--front { top: 43px; background: var(--ink); }
  .card--back { top: 527px; background: var(--ink); }
  .corner-flag { position: absolute; top: 0; right: 0; width: 116px; height: 121px; }
  .wordmark {
    position: absolute; font-weight: 400; line-height: 1;
    letter-spacing: 3px; white-space: nowrap;
  }
  .card--front .wordmark {
    left: 0; right: 0; text-align: center; top: 149px;
    font-size: 124px; color: var(--paper);
  }
  .front-url {
    position: absolute; left: 0; right: 0; top: 350px; text-align: center;
    color: var(--paper); font-size: 18px; letter-spacing: 1.5px;
  }
  .back-top {
    position: absolute; left: 0; top: 0; width: 100%; height: 209px;
    background: var(--paper);
  }
  .card--back .wordmark { left: 60px; top: 44px; font-size: 118px; color: var(--ink); }
  .divider-band {
    position: absolute; left: 0; top: 209px; width: 100%; height: 10px;
    background: var(--band);
  }
  .divider-pointer { position: absolute; left: 157px; top: 218px; width: 60px; height: 30px; }
  .person {
    position: absolute; left: 67px; width: 240px; text-align: center;
    color: var(--paper); white-space: nowrap;
  }
  .person__name { top: 277px; font-size: 24px; font-weight: 700; }
  .person__role { top: 307px; font-size: 18px; color: var(--accent); }
  .person__site { top: 367px; font-size: 19px; }
  .contact {
    position: absolute; left: 412px; top: 240px;
    color: var(--paper); font-size: 19px; line-height: 24px; white-space: nowrap;
  }
  .contact__company { color: var(--accent); }
  .contact__item { display: flex; align-items: center; gap: 8px; line-height: 25px; }
  .contact__item--first { margin-top: 4px; }
  .contact__icon { width: 17px; height: 14px; flex: none; }
</style>
</head>
<body>
<div class="canvas">

  <section class="card card--front">
    <svg class="corner-flag" viewBox="0 0 116 121" aria-hidden="true">
      <polygon points="0,0 116,0 116,121" fill="var(--accent)"/>
    </svg>
    <div class="wordmark">Tersyn</div>
    <div class="front-url">www.tersynworks.com</div>
  </section>

  <section class="card card--back">
    <div class="back-top"></div>
    <svg class="corner-flag" viewBox="0 0 116 121" aria-hidden="true">
      <polygon points="0,0 116,0 116,121" fill="var(--accent)"/>
    </svg>
    <div class="wordmark">Tersyn</div>
    <div class="divider-band"></div>
    <svg class="divider-pointer" viewBox="0 0 60 30" aria-hidden="true">
      <polygon points="0,0 60,0 30,29" fill="var(--band)"/>
    </svg>

    <div class="person person__name">Theo Marlowe</div>
    <div class="person person__role">Co Founder</div>
    <div class="person person__site">www.tersynworks.com</div>

    <div class="contact">
      <div class="contact__company">Tersyn Works, LLC</div>
      <div>482 Harlow Avenue, Suite 310</div>
      <div>Redfield, California 94077, USA</div>
      <div class="contact__item contact__item--first">
        <svg class="contact__icon" viewBox="0 0 17 14" aria-label="Phone">
          <path d="M1 5 Q8.5 -1 16 5 L16 7 L12 7 L12 5 Q8.5 3.5 5 5 L5 7 L1 7 Z" fill="var(--accent)"/>
          <rect x="4" y="7" width="9" height="6" rx="1" fill="var(--accent)"/>
        </svg>
        <span>(555) 214-7730</span>
      </div>
      <div class="contact__item">
        <svg class="contact__icon" viewBox="0 0 17 14" aria-label="Fax">
          <rect x="4" y="0" width="9" height="5" fill="var(--accent)"/>
          <rect x="1" y="5" width="15" height="7" rx="1" fill="var(--accent)"/>
          <rect x="4" y="9" width="9" height="5" fill="var(--ink)" stroke="var(--accent)" stroke-width="1.2"/>
        </svg>
        <span>(555) 214-7791</span>
      </div>
      <div class="contact__item">
        <svg class="contact__icon" viewBox="0 0 17 14" aria-label="Email">
          <rect x="0.5" y="1.5" width="16" height="11" fill="var(--accent)"/>
          <polyline points="0.5,1.5 8.5,8 16.5,1.5" fill="none" stroke="var(--ink)" stroke-width="1.3"/>
        </svg>
        <span>theo@tersynworks.com</span>
      </div>
    </div>
  </section>

</div>
</body>
</html>
```